Varlen Group Business Card design with current logo

hello all , we have abranded logo which i will attach but we need a card double sided designed . one side is easy as its the logo but the other side we want clean and modern. The info needed will be the same text as the card sample attached. no pictures of us though just clean and professinal pls. Logo can be incorporated on the text side to for recognition. Colors are Black , white , red and grey... ideal card would be matt finish high end stock. or a black card so white text ... Sorry i have uploaded al the files i got when I had the logo designed on here.. Oh forgot want to say pls add in the card details EST 1981 and over 40yrs combined experiance
Updates

Hello everyone , I'm really sorry we haven't been able to make a final decision.. There is at least 3 cards that all have there positives over the other two... We will decide by tonight.

Target Market(s)

20-70 wide range but people with money and a education.

Industry/Entity Type

Real Estate Agent

Contact Information for Business Card

One side the Logo choose from the different color logos, black being the one we like most, other side is the details. Clean professional looking fonts. EST 1981 , over 40yrs experiance. Website email and both names and PH# as per the sample card attached

Font styles to use
Other font styles liked:
• Fonts:Code Bold,Code Light, Lucida Fax.

Colors
1b1b1b
757575
c9c9c9
e8e8e8
ffffff
e9e9e9

Requirements
Must have
• Logo and contact info

```html
<!DOCTYPE html>
<html lang="en">
<head>
<meta charset="utf-8">
<title>Varlen Group Business Card</title>
<link rel="stylesheet" href="https://fonts.googleapis.com/css2?family=Cinzel:wght@400;600&family=Questrial&display=swap">
<style>
  :root {
    --ink: #2b2b2b;
    --charcoal: #1b1b1b;
    --grey: #757575;
    --silver: #b4b4b4;
    --light: #c9c9c9;
    --paper: #ffffff;
    --stage: #e9e9e9;
    --red: #c0272d;
  }
  * { margin: 0; padding: 0; box-sizing: border-box; }
  html, body { width: 1200px; height: 1100px; overflow: hidden; background: var(--stage); }
  .canvas { position: relative; width: 1200px; height: 1100px; }

  .card { position: absolute; left: 220px; width: 755px; height: 443px; overflow: hidden; }
  .card--front { top: 100px; background: var(--ink); }
  .card--back { top: 563px; background: var(--paper); }

  /* front: brand lockup */
  .brand-mark { position: absolute; background: var(--silver); border-radius: 4px; }
  .card--front .brand-mark { left: 175px; top: 133px; width: 150px; height: 157px; }
  .brand-name {
    position: absolute; font-family: "Questrial", sans-serif; line-height: 1;
    text-transform: uppercase; white-space: nowrap;
  }
  .card--front .brand-name { left: 345px; top: 175px; font-size: 58px; color: var(--silver); letter-spacing: 2px; }
  .card--front .brand-name span { display: block; }
  .card--front .brand-name .brand-sub { font-size: 34px; letter-spacing: 5px; margin-top: 14px; text-align: right; }

  /* back: dark panel */
  .back-panel { position: absolute; inset: 0; }
  .back-panel svg { display: block; }

  .card--back .brand-mark { left: 55px; top: 38px; width: 108px; height: 107px; background: var(--ink); border-radius: 3px; }
  .card--back .brand-name { left: 172px; top: 62px; font-size: 40px; color: var(--ink); letter-spacing: 1px; }
  .card--back .brand-name .brand-sub { display: block; font-size: 24px; letter-spacing: 3px; margin-top: 8px; text-align: right; }
  .established { position: absolute; left: 55px; top: 150px; font-family: "Cinzel", serif; font-size: 15px; color: var(--ink); }

  .experience {
    position: absolute; right: 57px; top: 68px; text-align: right;
    font-family: "Cinzel", serif; font-size: 15px; line-height: 19px; color: var(--light); letter-spacing: 0.5px;
  }

  .agent {
    position: absolute; right: 57px; font-family: "Cinzel", serif; font-size: 36px; color: var(--paper);
    line-height: 1; white-space: nowrap;
  }
  .agent--first { top: 177px; }
  .agent--second { top: 233px; }
  .divider { position: absolute; left: 406px; right: 0; top: 216px; height: 10px; background: var(--red); }

  .contact {
    position: absolute; right: 57px; top: 305px; text-align: right; list-style: none;
    font-family: "Cinzel", serif; font-weight: 600; font-size: 15px; line-height: 19px; color: var(--paper); letter-spacing: 0.5px;
  }

  .brokerage { position: absolute; left: 55px; top: 255px; display: flex; align-items: center; gap: 8px; }
  .brokerage-badge { width: 16px; height: 16px; background: var(--red); }
  .brokerage-name { font-family: "Cinzel", serif; font-weight: 600; font-size: 14px; color: var(--charcoal); }
  .office {
    position: absolute; left: 55px; top: 328px; font-style: normal;
    font-family: "Cinzel", serif; font-size: 17px; line-height: 21px; color: var(--ink);
  }
</style>
</head>
<body>
<main class="canvas">
  <section class="card card--front" aria-label="Card front">
    <div class="brand-mark"></div>
    <div class="brand-name"><span>Varlen</span><span class="brand-sub">Group</span></div>
  </section>

  <section class="card card--back" aria-label="Card back">
    <div class="back-panel">
      <svg width="755" height="443" viewBox="0 0 755 443" aria-hidden="true">
        <polygon points="755,0 247,232 378,232 378,443 755,443" fill="var(--ink)"/>
      </svg>
    </div>

    <div class="brand-mark"></div>
    <div class="brand-name">Varlen<span class="brand-sub">Group</span></div>
    <p class="established">EST 1981</p>

    <p class="experience">Over<br>40 Years<br>Combined<br>Experience</p>

    <p class="agent agent--first">Don Varlen</p>
    <div class="divider"></div>
    <p class="agent agent--second">Jordan Varlen</p>

    <ul class="contact">
      <li>Phone: 250-555-0148</li>
      <li>Fax: 250-555-0162</li>
      <li>Email: info@VarlenRealEstate.com</li>
      <li>Web: www.VarlenRealEstate.com</li>
    </ul>

    <div class="brokerage">
      <span class="brokerage-badge"></span>
      <span class="brokerage-name">Harbor Crest Realty</span>
    </div>
    <address class="office">Harbor Crest Realty<br>210-3380 Linden Way<br>Victoria BC V8X 2K4</address>
  </section>
</main>
</body>
</html>
```